GUARANTEED! Simple website for independent event planner and consultant...

I need a website that is no more than 5 or 6 pages to illustrate who I am and what I can offer to groups who book hotels for meetings and conferences. I have 20 years of experience planning meetings within hotels and I am now ready to go out on my own and help clients choose venues, negotiate contracts and plan effective meetings. I will focus on clients planning meetings in the mountains of Colorado but I am willing to travel as well. I want to work with a person who is collaborative and can direct me on what they need to move the project along quickly. I already have my logo, a hosting site and work e-mail address. Also, I recently hired a photographer to do head shots. Lastly, it important for me to be able to talk on the phone or skype with this person, as needed and I must be able to make changes to my site down the road when necessary...

Target Market(s)

Corporate Groups

Industry/Entity Type

Event Planning

Coding

Coded - Design and coding required

Number of Pages Required

5+ page

Font styles to use
Sans Serif

Requirements
Must have
• About me page, event planning services offered page, task force and consulting work page, testimonials page, page for blogs, page to contact me/request a proposal. May need advice on what else I need...
Nice to have
• I want it to look sharp and professional. I want people to look at my site and know immediately that they can trust me and the work I can do.
• I don't want it to look like it is over the top as I am not a HUGE company but I do want it to be professional and easy to view and navigate.
Should not have
• Bright colors
• My logo is bright orange and black. I have also used dark grey and orange. See below:
• Orange:
• C = 0
• M = 64
• Y = 100
• K = 0
• Gray:
• C = 67
• M = 60
• Y = 59
• K = 45
• Font: Gotham Book and Gotham Bold

```html
<!DOCTYPE html>
<html lang="en">
<head>
<meta charset="utf-8">
<title>Harlow Event Management – Blog</title>
<link href="https://fonts.googleapis.com/css2?family=Montserrat:wght@500;600&family=Raleway:wght@400;500&family=Open+Sans:wght@400&display=swap" rel="stylesheet">
<style>
  :root {
    --orange: #f5821f;
    --ink: #222222;
    --text: #555555;
    --muted: #8a8a8a;
    --page: #f1f1f1;
    --card: #ffffff;
    --footer: #141414;
    --rule: #f5821f;
  }
  * { box-sizing: border-box; margin: 0; padding: 0; }
  html, body { width: 1200px; height: 664px; overflow: hidden; }
  body { position: relative; background: var(--page); font-family: "Open Sans", Arial, sans-serif; color: var(--text); }

  .sidebar { position: absolute; left: 0; top: 0; width: 225px; height: 664px; background: #fff; }
  .brand { position: absolute; left: 28px; top: 46px; width: 150px; color: var(--orange); font-family: "Montserrat", Arial, sans-serif; font-weight: 600; line-height: 1.15; }
  .brand-name { display: block; font-size: 27px; letter-spacing: 1px; }
  .brand-sub { display: block; font-size: 8.6px; letter-spacing: 1.3px; margin-top: 3px; }

  .nav { position: absolute; left: 26px; top: 164px; width: 154px; list-style: none; }
  .nav li { height: 45px; border-bottom: 1px solid var(--rule); margin-bottom: 0; padding-top: 0; }
  .nav li + li { padding-top: 0; }
  .nav li { display: flex; flex-direction: column; justify-content: flex-start; }
  .nav-title { font-family: "Raleway", Arial, sans-serif; font-weight: 500; font-size: 13.5px; color: var(--ink); line-height: 16px; margin-top: 0; }
  .nav-sub { font-family: "Raleway", Arial, sans-serif; font-size: 9.8px; color: #444; line-height: 13px; }
  .nav li:last-child { border-bottom: none; }

  .social { position: absolute; left: 0; top: 494px; width: 225px; height: 43px; background: var(--orange); display: flex; justify-content: space-around; align-items: center; padding: 0 18px; }
  .social-dot { width: 10px; height: 10px; border-radius: 50%; background: #fff; }

  .card { position: absolute; background: var(--card); overflow: hidden; }
  .card-photo { display: block; width: 100%; }
  .card-body { padding: 0 14px; }
  .card-title { font-size: 12px; color: var(--ink); font-weight: 400; line-height: 16px; }
  .card-text { font-size: 9.8px; line-height: 16px; color: var(--text); }
  .card-date { font-size: 8px; color: var(--muted); line-height: 14px; margin-top: 1px; }
  .card.centered { text-align: center; }
  .card-icon { width: 45px; height: 45px; border-radius: 50%; border: 1px solid #e2e2e2; margin: 0 auto; display: flex; align-items: center; justify-content: center; }

  .footer { position: absolute; left: 225px; top: 636px; width: 975px; height: 28px; background: var(--footer); }
  .footer p { position: absolute; left: 43px; top: 9px; font-family: "Raleway", Arial, sans-serif; font-size: 8.4px; color: var(--orange); }
</style>
</head>
<body>
  <aside class="sidebar">
    <div class="brand">
      <span class="brand-name">HARLOW</span>
      <span class="brand-sub">EVENT MANAGEMENT</span>
    </div>
    <ul class="nav">
      <li><span class="nav-title">HOME</span><span class="nav-sub">Harlow Event Management</span></li>
      <li><span class="nav-title">ABOUT</span><span class="nav-sub">Me and My Experiences</span></li>
      <li><span class="nav-title">SERVICES</span><span class="nav-sub">What I can Offer</span></li>
      <li><span class="nav-title">CONSULTING</span><span class="nav-sub">Giving you best Advice</span></li>
      <li><span class="nav-title">TESTIMONIALS</span><span class="nav-sub">What they Say</span></li>
      <li><span class="nav-title">BLOGS</span><span class="nav-sub">Whats Happening</span></li>
      <li><span class="nav-title">CONTACT</span><span class="nav-sub">Let's Talk</span></li>
    </ul>
    <div class="social">
      <span class="social-dot"></span><span class="social-dot"></span><span class="social-dot"></span>
    </div>
  </aside>

  <article class="card" style="left:242px; top:16px; width:464px; height:368px;">
    <div class="card-photo" role="img" aria-label="Business team meeting around a conference table" style="height:289px; background:linear-gradient(135deg,#dfe6ea 0%,#c9d2d8 40%,#3a3f48 75%,#e8ecee 100%);"></div>
    <div class="card-body" style="padding-top:16px;">
      <h2 class="card-title">A really simple entry</h2>
      <p class="card-text">Lorem ipsum dolor sit amet, consectetuer adipiscing elit. Aenean...</p>
      <p class="card-date">September 29, 2014</p>
    </div>
  </article>

  <article class="card centered" style="left:718px; top:16px; width:225px; height:177px; padding-top:34px;">
    <div class="card-icon">
      <svg width="22" height="18" viewBox="0 0 22 18" fill="none" stroke="#777" stroke-width="1.6"><rect x="2" y="4" width="18" height="12"/><path d="M4 14l5-5 4 4 3-2 3 3"/><path d="M5 4l9-3 2 3"/></svg>
    </div>
    <h2 class="card-title" style="margin-top:10px;">Gallery of the ages</h2>
    <p class="card-text">Nulla consequat massa quis</p>
    <p class="card-date">September 29, 2014</p>
  </article>

  <article class="card centered" style="left:955px; top:16px; width:225px; height:177px; padding-top:14px;">
    <div class="card-icon">
      <svg width="22" height="16" viewBox="0 0 22 16"><rect x="1" y="1" width="20" height="14" fill="#777"/><path d="M9 5l6 3-6 3z" fill="#fff"/></svg>
    </div>
    <h2 class="card-title" style="margin-top:10px;">A cool video entry</h2>
    <p class="card-text">http://clipvault.net/groups/stockfootage<br>/videos/41629603</p>
    <p class="card-text" style="margin-top:16px;">Lorem ipsum...</p>
    <p class="card-date">September 29, 2014</p>
  </article>

  <article class="card centered" style="left:718px; top:206px; width:225px; height:177px; padding:56px 16px 0;">
    <h2 class="card-title">Entry without preview image</h2>
    <p class="card-text">Lorem ipsum dolor sit amet, consectetuer adipiscing elit. Aenean...</p>
    <p class="card-date">September 29, 2014</p>
  </article>

  <article class="card" style="left:955px; top:206px; width:225px; height:368px;">
    <div class="card-photo" role="img" aria-label="Two colleagues smiling while working on a laptop" style="height:272px; background:linear-gradient(160deg,#6e6a66 0%,#a49c94 35%,#3a3c44 70%,#cfd1d3 100%);"></div>
    <div class="card-body" style="padding-top:14px;">
      <h2 class="card-title">Jazzy Jazz, music at its best</h2>
      <p class="card-text">Lorem ipsum dolor sit amet, consectetuer adipiscing elit....</p>
      <p class="card-date">September 29, 2014</p>
    </div>
  </article>

  <article class="card" style="left:242px; top:396px; width:464px; height:177px;">
    <div class="card-photo" role="img" aria-label="Business people talking in a bright office lobby" style="height:98px; background:linear-gradient(90deg,#2f3440 0%,#d9dee2 45%,#f2f4f5 70%,#a8b54a 85%,#eef0f0 100%);"></div>
    <div class="card-body" style="padding-top:18px;">
      <h2 class="card-title">A nice post</h2>
      <p class="card-text">Donec posuere vulputate arcu.</p>
      <p class="card-date">September 29, 2014</p>
    </div>
  </article>

  <article class="card" style="left:718px; top:396px; width:225px; height:177px;">
    <div class="card-photo" role="img" aria-label="Smiling business leader with two colleagues" style="height:98px; background:linear-gradient(90deg,#c9c9c9 0%,#9aa0a8 40%,#3c4250 60%,#d4d4d4 100%);"></div>
    <div class="card-body" style="padding-top:18px;">
      <h2 class="card-title">A nice entry</h2>
      <p class="card-text">Nulla consequat massa quis enim.</p>
      <p class="card-date">September 29, 2014</p>
    </div>
  </article>

  <footer class="footer">
    <p>© Copyright 2017 - Harlow Event Management</p>
  </footer>
</body>
</html>
```